Commercial Loan Originator Business Card (CHANGE COLORS SCHEME)

CHANGE COLOR SCHEME - SAME DESIGN

Name Marissa Lantham
Title Commercial Loan Originator
Office (800) 641-2905 x68
Direct (240) 617-2435
Email brightleaf4you@mailpost.example

Name Derek Fallow
Office (800) 641-2905 x70
Direct (410) 932-1864
Email d.falthebroker@mailpost.example

Name Gordon Wexley
Office (800) 641-2905 x71
Direct (215) 346-2081
Email g.wexley37@mailpost.example

Name Lyn Moreau
Office (800) 641-2905 x
Direct (202) 458-1937
Email lmoreau64@mailpost.example

Name Nadia Strand
Office (800) 641-2905 x72
Direct (240) 871-5246
Email qrzhomelending@mailpost.example

```html
<!DOCTYPE html>
<html lang="en">
<head>
<meta charset="utf-8">
<title>Commercial Loan Originator Business Cards</title>
<link rel="stylesheet" href="https://fonts.googleapis.com/css2?family=Montserrat:wght@400;700&display=swap">
<style>
  :root {
    --backdrop-top: #d2d2d2;
    --backdrop-bottom: #a3a3a3;
    --card: #ffffff;
    --accent: #9dc93b;
    --ink: #1d1d1d;
    --shadow: rgba(0, 0, 0, 0.28);
  }
  * { box-sizing: border-box; margin: 0; padding: 0; }
  html, body { width: 1200px; height: 1194px; overflow: hidden; }
  body {
    position: relative;
    background: linear-gradient(180deg, var(--backdrop-top), var(--backdrop-bottom));
    font-family: "Montserrat", Arial, sans-serif;
    color: var(--ink);
  }
  .card {
    position: absolute;
    width: 509px;
    height: 291px;
    background: var(--card);
    border-radius: 26px;
    overflow: hidden;
    box-shadow: 0 6px 14px var(--shadow);
  }
  .card--gordon  { left: 70px;  top: 95px; }
  .card--marissa { left: 620px; top: 98px; }
  .card--derek   { left: 70px;  top: 450px; }
  .card--lyn     { left: 620px; top: 453px; }
  .card--nadia   { left: 345px; top: 807px; }

  .card__name {
    position: absolute;
    left: 29px; top: 31px;
    font-weight: 700;
    font-size: 22px;
    line-height: 1;
    color: var(--accent);
    text-transform: uppercase;
    letter-spacing: 0.2px;
  }
  .card__title {
    position: absolute;
    left: 29px; top: 55px;
    font-size: 13.5px;
    line-height: 1;
  }
  .contact {
    position: absolute;
    left: 29px; top: 199px;
    list-style: none;
  }
  .contact__item {
    display: flex;
    align-items: center;
    height: 23.5px;
    font-size: 13.5px;
    white-space: nowrap;
  }
  .contact__icon {
    width: 11px; height: 11px;
    margin-right: 6px;
    fill: var(--accent);
    flex: none;
  }
  .portrait {
    position: absolute;
    right: 0; bottom: 0;
  }
  .card--gordon .portrait  { left: 289px; top: 31px; background: linear-gradient(180deg, #ffffff 0%, #6b4a3a 25%, #1f2b4d 70%); }
  .card--marissa .portrait { left: 307px; top: 46px; background: linear-gradient(180deg, #ffffff 0%, #6a4636 30%, #e0338c 65%); }
  .card--derek .portrait   { left: 285px; top: 37px; background: linear-gradient(180deg, #ffffff 0%, #5d4033 25%, #4a5446 65%); }
  .card--lyn .portrait     { left: 293px; top: 81px; background: linear-gradient(180deg, #ffffff 0%, #5b3b30 30%, #7a3f78 80%); }
  .card--nadia .portrait   { left: 310px; top: 53px; background: linear-gradient(180deg, #ffffff 0%, #8a3a3e 20%, #222222 55%); }
</style>
</head>
<body>
<svg width="0" height="0" style="position:absolute" aria-hidden="true">
  <defs>
    <symbol id="icon-phone" viewBox="0 0 24 24"><path d="M6.6 10.8a15 15 0 0 0 6.6 6.6l2.2-2.2c.3-.3.7-.4 1-.2 1.1.4 2.3.6 3.6.6.6 0 1 .4 1 1V20c0 .6-.4 1-1 1A17 17 0 0 1 3 4c0-.6.4-1 1-1h3.5c.6 0 1 .4 1 1 0 1.3.2 2.5.6 3.6.1.3 0 .7-.2 1z"/></symbol>
    <symbol id="icon-mobile" viewBox="0 0 24 24"><path d="M7 1h10a2 2 0 0 1 2 2v18a2 2 0 0 1-2 2H7a2 2 0 0 1-2-2V3a2 2 0 0 1 2-2zm0 3v14h10V4z"/></symbol>
    <symbol id="icon-mail" viewBox="0 0 24 24"><path d="M2 5h20v14H2zm2 2v.5l8 5 8-5V7l-8 5z"/></symbol>
  </defs>
</svg>

<article class="card card--gordon">
  <h2 class="card__name">Gordon Wexley</h2>
  <p class="card__title">Commercial Loan Originator</p>
  <ul class="contact">
    <li class="contact__item"><svg class="contact__icon"><use href="#icon-phone"/></svg>(800) 641-2905 x71</li>
    <li class="contact__item"><svg class="contact__icon"><use href="#icon-mobile"/></svg>(215) 346-2081</li>
    <li class="contact__item"><svg class="contact__icon"><use href="#icon-mail"/></svg>g.wexley37@mailpost.example</li>
  </ul>
  <div class="portrait" role="img" aria-label="Portrait photo of Gordon Wexley in a navy suit and tie"></div>
</article>

<article class="card card--marissa">
  <h2 class="card__name">Marissa Lantham</h2>
  <p class="card__title">Commercial Loan Originator</p>
  <ul class="contact">
    <li class="contact__item"><svg class="contact__icon"><use href="#icon-phone"/></svg>(800) 641-2905 x68</li>
    <li class="contact__item"><svg class="contact__icon"><use href="#icon-mobile"/></svg>(240) 617-2435</li>
    <li class="contact__item"><svg class="contact__icon"><use href="#icon-mail"/></svg>brightleaf4you@mailpost.example</li>
  </ul>
  <div class="portrait" role="img" aria-label="Portrait photo of Marissa Lantham in a pink top"></div>
</article>

<article class="card card--derek">
  <h2 class="card__name">Derek Fallow</h2>
  <p class="card__title">Commercial Loan Originator</p>
  <ul class="contact">
    <li class="contact__item"><svg class="contact__icon"><use href="#icon-phone"/></svg>(800) 641-2905 x70</li>
    <li class="contact__item"><svg class="contact__icon"><use href="#icon-mobile"/></svg>(410) 932-1864</li>
    <li class="contact__item"><svg class="contact__icon"><use href="#icon-mail"/></svg>d.falthebroker@mailpost.example</li>
  </ul>
  <div class="portrait" role="img" aria-label="Portrait photo of Derek Fallow in a green plaid blazer"></div>
</article>

<article class="card card--lyn">
  <h2 class="card__name">Lyn Moreau</h2>
  <p class="card__title">Commercial Loan Originator</p>
  <ul class="contact">
    <li class="contact__item"><svg class="contact__icon"><use href="#icon-phone"/></svg>(800) 641-2905 x</li>
    <li class="contact__item"><svg class="contact__icon"><use href="#icon-mobile"/></svg>(202) 458-1937</li>
    <li class="contact__item"><svg class="contact__icon"><use href="#icon-mail"/></svg>lmoreau64@mailpost.example</li>
  </ul>
  <div class="portrait" role="img" aria-label="Portrait photo of Lyn Moreau in glasses and a patterned blouse"></div>
</article>

<article class="card card--nadia">
  <h2 class="card__name">Nadia Strand</h2>
  <p class="card__title">Commercial Loan Originator</p>
  <ul class="contact">
    <li class="contact__item"><svg class="contact__icon"><use href="#icon-phone"/></svg>(800) 641-2905 x72</li>
    <li class="contact__item"><svg class="contact__icon"><use href="#icon-mobile"/></svg>(240) 871-5246</li>
    <li class="contact__item"><svg class="contact__icon"><use href="#icon-mail"/></svg>qrzhomelending@mailpost.example</li>
  </ul>
  <div class="portrait" role="img" aria-label="Seated portrait photo of Nadia Strand in a black ruffled top"></div>
</article>
</body>
</html>
```